New Full Color Flyer for Mailing Program

I have a flyer already for a program I launching. I am in need of a professional to use my flyer to create a much more leaner flyer. The new flyer should convey a message through the use of graphics rather then words.
The goal is to incite the reader to get excited and buy in, but at the same time explain the products that are included with a purchase.
Attached is my own flyer to be used as a reference point. I allow you to make suggestions to me to consider for the flyer and changes you think will perform well.
MUST BE PSD SOURCE & is expected to be handed over at the end.
Target Market(s)
Home business and income opportunity buyers
Industry/Entity Type
Small Business
Colors
Designer to choose colors to be used in the design.
Requirements
Must have
- Exciting Graphics/cartoons that convey success, money and riches. Should look good in color and gray/white.
- Level Payouts
- Order Form
- THE BRIGHT MAPLE METHOD
Nice to have
- crisp clean text

```html
<!DOCTYPE html>
<html lang="en">
<head>
<meta charset="utf-8">
<title>The Bright Maple Method – Mailing Flyer</title>
<link href="https://fonts.googleapis.com/css2?family=Arimo:wght@400;700&family=Lato:wght@400;700&display=swap" rel="stylesheet">
<style>
  :root{
    --navy:#0b1b95;
    --red:#e3060f;
    --ink:#555a5e;
    --slate:#3b3b6b;
    --paper:#ffffff;
    --backdrop:#d6d6d6;
    --gold:#e7b93a;
    --cash:#bfe3a6;
  }
  *{margin:0;padding:0;box-sizing:border-box}
  html,body{width:1200px;height:1200px;overflow:hidden;background:var(--backdrop)}
  .flyer{position:absolute;left:20px;top:225px;width:1160px;height:751px;background:var(--paper);font-family:'Lato',sans-serif;color:var(--ink)}
  .masthead{position:absolute;left:0;top:0;width:100%;height:132px;background:var(--navy)}
  .flag{position:absolute;top:39px;width:113px;height:58px;background:linear-gradient(180deg,#c8102e 0 14%,#fff 14% 28%,#c8102e 28% 42%,#fff 42% 56%,#c8102e 56% 70%,#fff 70% 84%,#c8102e 84%)}
  .flag-left{left:75px}
  .flag-right{right:65px}
  .brand-title{position:absolute;left:0;width:100%;top:32px;text-align:center;font-family:'Arimo',sans-serif;font-weight:700;font-size:54px;line-height:60px;color:var(--red);letter-spacing:0.5px}
  .brand-tagline{position:absolute;left:0;width:100%;top:93px;text-align:center;font-family:'Arimo',sans-serif;font-size:28px;line-height:32px;color:#fff}
  .headline{position:absolute;left:0;width:100%;top:145px;text-align:center;font-family:'Arimo',sans-serif;font-weight:700;font-size:33px;line-height:41px;color:var(--ink)}
  .hot{color:var(--red)}
  .intro{position:absolute;left:40px;top:241px;width:1081px;font-size:18.6px;line-height:22.7px;text-align:justify}
  .intro b,.pay-copy b{color:var(--red);font-weight:700}
  .offer-title{position:absolute;left:100px;width:504px;top:327px;text-align:center;font-family:'Arimo',sans-serif;font-weight:700;font-size:34px;line-height:43px;color:var(--red)}
  .offer-title .sub{display:block;color:var(--slate)}
  .offer-note{position:absolute;left:50px;width:318px;top:418px;text-align:center;font-size:18.5px;line-height:22.7px}
  .offer-note p+p{margin-top:12px}
  .arrow{position:absolute;left:383px;top:443px;width:70px;height:48px}
  .levels{position:absolute;left:501px;top:418px;font-size:18.5px;line-height:22.7px;list-style:none}
  .art{position:absolute;border-radius:10px}
  .art-treasure{left:81px;top:515px;width:263px;height:204px;background:radial-gradient(ellipse at 50% 75%,var(--gold),#c9a062 60%,rgba(255,255,255,0) 72%)}
  .art-cash{left:412px;top:521px;width:226px;height:184px;background:radial-gradient(ellipse at 50% 78%,var(--cash),#8fa06a 55%,rgba(255,255,255,0) 72%)}
  .pay-box{position:absolute;left:720px;top:334px;width:399px;height:378px;border:2.5px dashed var(--red)}
  .pay-label{position:absolute;left:22px;top:13px;width:357px;height:45px;background:var(--navy);color:#fff;font-family:'Arimo',sans-serif;font-weight:700;font-size:34px;line-height:45px;text-align:center}
  .pay-copy{position:absolute;left:25px;top:72px;width:347px;font-size:18.2px;line-height:22.7px;text-align:justify}
  .perks{position:absolute;left:34px;top:201px;list-style:none;font-size:18.5px}
  .perks li{display:flex;align-items:center;height:34.3px}
  .perks svg{width:20px;height:20px;margin-right:16px;flex:none}
</style>
</head>
<body>
<main class="flyer">
  <header class="masthead">
    <div class="flag flag-left" role="img" aria-label="Stars and stripes flag"></div>
    <h1 class="brand-title">BRIGHT MAPLE METHOD</h1>
    <p class="brand-tagline">Quick &amp; Simple Cash Generator!</p>
    <div class="flag flag-right" role="img" aria-label="Stars and stripes flag"></div>
  </header>

  <h2 class="headline">GENERATE A <span class="hot">TSUNAMI</span> OF $500+<br>CASH &amp; MONEY ORDER PAYMENTS DAILY</h2>

  <p class="intro"><b>BRIGHT MAPLE METHOD</b> is an exciting program paying <b>UNLIMITED</b> commissions to businesses and ordinary Joes around the country to resell our online profits how-to reports &amp; training manuals. You just mail this flyer and collect the direct payments. If you can mail a flyer, this is for you...do not miss this opportunity!</p>

  <h3 class="offer-title">The BRIGHT MAPLE METHOD<span class="sub">Limits are ENDLESS!!!</span></h3>
  <div class="offer-note">
    <p>LOOK!!! The $500 Program rewards handsomly.</p>
    <p>Based on 10 Who get 10</p>
  </div>
  <svg class="arrow" viewBox="0 0 70 48" aria-hidden="true"><path d="M0 14H38V0L70 24 38 48V34H0Z" fill="#e3060f"/></svg>
  <ul class="levels">
    <li>Level 1 = $5,000</li>
    <li>Level 2 = $50,000</li>
    <li>Level 3 = $500,000</li>
    <li>Level 4 = $5,000,000</li>
  </ul>

  <div class="art art-treasure" role="img" aria-label="Cartoon businessman cheering on a pile of gold coins and jewels"></div>
  <div class="art art-cash" role="img" aria-label="Cartoon businessman relaxing on a stack of banknotes"></div>

  <section class="pay-box">
    <h3 class="pay-label">ENDLESS PAY PLAN</h3>
    <p class="pay-copy">You are paid commrssrons on <b>4 Levels</b> and your name Will continue to be onto your teams flyers throough infinity. Your talking <b>THOUSANDS</b> of flyers With your name making you <b>CASH</b>...That is <b>Power</b>!!!</p>
    <ul class="perks">
      <li><svg viewBox="0 0 20 20"><path d="M16 2H2V18H18V10" fill="none" stroke="#0b1b95" stroke-width="2"/><path d="M6 9l4 4 9-10" fill="none" stroke="#0b1b95" stroke-width="2"/></svg>Affordable Income Opportunity</li>
      <li><svg viewBox="0 0 20 20"><path d="M16 2H2V18H18V10" fill="none" stroke="#0b1b95" stroke-width="2"/><path d="M6 9l4 4 9-10" fill="none" stroke="#0b1b95" stroke-width="2"/></svg>Company Support</li>
      <li><svg viewBox="0 0 20 20"><path d="M16 2H2V18H18V10" fill="none" stroke="#0b1b95" stroke-width="2"/><path d="M6 9l4 4 9-10" fill="none" stroke="#0b1b95" stroke-width="2"/></svg>Simple To Earn, No monthly fee</li>
      <li><svg viewBox="0 0 20 20"><path d="M16 2H2V18H18V10" fill="none" stroke="#0b1b95" stroke-width="2"/><path d="M6 9l4 4 9-10" fill="none" stroke="#0b1b95" stroke-width="2"/></svg>Updated and Fresh Products</li>
      <li><svg viewBox="0 0 20 20"><path d="M16 2H2V18H18V10" fill="none" stroke="#0b1b95" stroke-width="2"/><path d="M6 9l4 4 9-10" fill="none" stroke="#0b1b95" stroke-width="2"/></svg>Unlimited &amp; Direct Payments</li>
    </ul>
  </section>
</main>
</body>
</html>
```